Business card design needed

Family General Practitioner/ Family Physician.
Logo is the logo of the Imperial Guild of Community Clinicians Oceania
http://pkvtm.lorimar.example/PictureGallery/logos/pages/IGCCO%20logo_jpg.htm

Reason: Just a bit more time to make changes and the weekend for me to look at things closely and to choose. Thanks, Ulan

Thanks for all the submissions. So many of them are really works of art. Not one of them are not good. The ones that I am eliminating are the ones that I think are not suitable for me personally only, and because if I don't, it makes it very difficult to decide as many of you are also sending me slight variations of a card. I have just decided to choose a second place card too. Can't thank you all enough. Good luck, Ulan. P.S - Working today till 10 pm as the card says :-), so probably won't be able to give a feedback till late Saturday night or Sunday morning here in Sydney, Australia. 

Reason: Just added a second place to the budget and realised that Australia is ahead of the rest of the world in the time zone (only :-) - don't want to offend anyone or start a debate!! ) , so Monday deadline will mean it will be a weekend for the rest of the world. Just wanted to give everyone more time to submit their best, especially since I will be picking a second card too. Can't thank everyone enough for the submissions. P.S - Not keen on photos on the card.

Business

Contact Information for Business Card

Dr. Ulan Pereira M.B.B.S., F.I.G.C.C.O
Family General Practitioner
Address, timings, phone and fax number on the back.

Requirements
Must have
• Timings
Mon 7 am - 7 pm
Tues 7 am - 12 pm
Wed 7 am - 10 pm
Thurs 7 am - 12 pm
Fri 7 am - 8 pm
Sat 8 am - 10 pm
Sun - Off

```html
<!DOCTYPE html>
<html lang="en">
<head>
<meta charset="utf-8">
<title>Dr Ulan Pereira – Business Card</title>
<link rel="stylesheet" href="https://fonts.googleapis.com/css2?family=Bodoni+Moda:wght@400&display=swap">
<style>
  :root {
    --ink: #1d1d1d;
    --accent-red: #e8322f;
    --frame: #9fb0b8;
    --crest-faint: #d6d6d6;
    --card-grey: #a9aeb3;
    --paper: #ffffff;
  }
  html, body {
    margin: 0;
    padding: 0;
    overflow: hidden;
    background: var(--paper);
  }
  .canvas {
    position: relative;
    width: 1200px;
    height: 736px;
    overflow: hidden;
    background: var(--paper);
    font-family: "Bodoni Moda", "Didot", serif;
    color: var(--ink);
  }
  .abs { position: absolute; margin: 0; white-space: nowrap; }

  /* ---------- Classic white version ---------- */
  .classic-front {
    left: 33px; top: 95px; width: 490px; height: 265px;
    border: 1.5px solid var(--frame);
    box-sizing: border-box;
  }
  .classic-back {
    left: 20px; top: 407px; width: 492px; height: 266px;
    border: 1.5px solid var(--frame);
    box-sizing: border-box;
  }
  .crest-decoration {
    background: linear-gradient(160deg, #e4e4e4 0%, var(--crest-faint) 60%, #e9e9e9 100%);
  }
  .crest-decoration.front { left: 158px; top: 15px; width: 132px; height: 260px; border-radius: 8px 8px 60px 60px; }
  .crest-decoration.back { left: 375px; top: 408px; width: 136px; height: 262px; border-radius: 60px 8px 8px 8px; }

  .guild-mark {
    display: flex; align-items: center; gap: 6px;
    font-size: 15px; color: var(--ink);
  }
  .guild-mark .dot {
    width: 14px; height: 14px; border-radius: 50%;
    background: var(--ink);
  }

  .doctor-name { font-size: 30px; line-height: 1; letter-spacing: 0.2px; font-weight: 400; }
  .credentials { font-size: 15px; line-height: 1; letter-spacing: 0.6px; }
  .role { font-size: 18px; line-height: 1; letter-spacing: 0.4px; }

  .hours { list-style: none; padding: 0; font-size: 17px; line-height: 22.4px; }
  .hours li { margin: 0; }
  .hours.compact { font-size: 16px; line-height: 21px; }

  .address { font-size: 12.5px; line-height: 13px; }
  .phones { font-size: 11px; color: var(--accent-red); letter-spacing: -0.2px; }

  /* ---------- Grey version ---------- */
  .grey-front {
    left: 650px; top: 75px; width: 513px; height: 288px;
    border-radius: 26px;
    background: var(--card-grey);
  }
  .grey-back {
    left: 665px; top: 415px; width: 487px; height: 290px;
    border-radius: 26px;
    background: var(--card-grey);
  }
</style>
</head>
<body>
<main class="canvas">

  <!-- Classic white card: front -->
  <div class="abs crest-decoration front" role="img" aria-label="Large faint grey heraldic crest decoration"></div>
  <section class="abs classic-front" aria-label="Front of card, white version"></section>
  <div class="abs guild-mark" style="left:420px; top:140px;"><span class="dot"></span>IGCCO</div>
  <h1 class="abs doctor-name" style="right:685px; top:272px;">Dr Ulan Pereira</h1>
  <p class="abs credentials" style="right:685px; top:302px;">M.B.B.S., F.I.G.C.C.O</p>
  <p class="abs role" style="right:685px; top:334px;">FAMILY GENERAL PRACTITIONER</p>

  <!-- Classic white card: back -->
  <section class="abs classic-back" aria-label="Back of card, white version"></section>
  <div class="abs crest-decoration back" role="img" aria-label="Large faint grey heraldic crest decoration"></div>
  <ul class="abs hours compact" style="left:28px; top:417px;">
    <li>Working Hours</li>
    <li>Mon 7 am - 7 pm.</li>
    <li>Tues 7 am - 12 pm.</li>
    <li>Wed 7 am - 10 pm.</li>
    <li>Thurs 7 am - 12 pm.</li>
    <li>Fri 7 am - 8 pm.</li>
    <li>Sat 8 am - 10 pm.</li>
    <li>Sun - Off.</li>
  </ul>
  <p class="abs address" style="left:28px; top:609px;">Level 2, Harbour Lane, Willowmere Plaza Centre<br>Brookvale Heights, NSW 2199</p>
  <p class="abs phones" style="left:28px; top:648px;">P: 02 9471 5830&nbsp;&nbsp; F: 02 9471 5831</p>

  <!-- Grey card: front -->
  <section class="abs grey-front" role="img" aria-label="Grey card face with soft animal-spot pattern"></section>
  <div class="abs guild-mark" style="left:1020px; top:151px; font-size:17px;"><span class="dot"></span>IGCCO</div>
  <h2 class="abs doctor-name" style="left:678px; top:248px; font-size:32px;">Dr Ulan Pereira</h2>
  <p class="abs credentials" style="left:679px; top:278px; font-size:16.5px; letter-spacing:0.8px;">M.B.B.S., F.I.G.C.C.O</p>
  <p class="abs role" style="left:679px; top:314px; font-size:19px;">FAMILY GENERAL PRACTITIONER</p>

  <!-- Grey card: back -->
  <section class="abs grey-back" role="img" aria-label="Grey card back with soft animal-spot pattern"></section>
  <ul class="abs hours" style="left:667px; top:429px;">
    <li>Working Hours</li>
    <li>Mon 7 am - 7 pm.</li>
    <li>Tues 7 am - 12 pm.</li>
    <li>Wed 7 am - 10 pm.</li>
    <li>Thurs 7 am - 12 pm.</li>
    <li>Fri 7 am - 8 pm.</li>
    <li>Sat 8 am - 10 pm.</li>
    <li>Sun - Off.</li>
  </ul>
  <p class="abs address" style="left:667px; top:624px; font-size:13.5px; line-height:15px;">Level 2, Harbour Lane, Willowmere Plaza Centre<br>Brookvale Heights, NSW 2199</p>
  <p class="abs phones" style="left:667px; top:671px; font-size:12.5px;">P: 02 9471 5830&nbsp;&nbsp; F: 02 9471 5831</p>

</main>
</body>
</html>
```